Graphic Design Project-Label for New Bourbon

Hi Designers

This is a new label for a Bourbon .Im looking for a smart looking label, Mordern,Simple .Clean.

Bottle type is the same as Harlow Gin Bottle if you google or can use others bottles glass.

I am open to new bourbon names and would love to see your creativity.

The Label Name is currently called Copper Ridge
Size is 1 litre.
Percentage is 37.5%.
Updates

Target Market(s)

ALL bourbon drinkers

Industry/Entity Type

Graphic Design

Requirements
Must have
• Up on top chosen label will send ingrediance final changes

```html
<!DOCTYPE html>
<html lang="en">
<head>
<meta charset="utf-8">
<title>Copper Ridge Bourbon – Label Set</title>
<link rel="stylesheet" href="https://fonts.googleapis.com/css2?family=Cinzel:wght@400&family=Alfa+Slab+One&display=swap">
<style>
  :root {
    --bg-light: #ececec;
    --bg-mid: #c6c6c6;
    --bg-dark: #a6a6a6;
    --gold: #d2b176;
    --gold-deep: #b88f4f;
    --ink: #141414;
    --paper: #fffdf7;
    --cream: #fdf1d8;
    --sun: #f1d4a2;
    --barrel: #e2a968;
  }
  html, body {
    margin: 0;
    padding: 0;
    overflow: hidden;
  }
  .canvas {
    position: relative;
    width: 1166px;
    height: 1200px;
    overflow: hidden;
    background: radial-gradient(ellipse at 25% 25%, var(--bg-light) 0%, var(--bg-mid) 55%, var(--bg-dark) 100%);
  }
  .symbol-library {
    position: absolute;
    width: 0;
    height: 0;
    overflow: hidden;
  }
  .brand-title {
    position: absolute;
    margin: 0;
    text-align: center;
    font-family: "Cinzel", serif;
    font-weight: 400;
    line-height: 1.1;
    color: var(--gold);
  }
  .brand-title--large {
    left: 730px;
    top: 30px;
    width: 420px;
    font-size: 58px;
    letter-spacing: 1px;
  }
  .brand-title--small {
    left: 58px;
    top: 462px;
    width: 310px;
    font-size: 40px;
    letter-spacing: 1px;
  }
  .neck-label,
  .front-label {
    position: absolute;
    display: block;
  }
  .neck-label--large { left: 402px; top: 162px; width: 328px; height: 203px; }
  .neck-label--small { left: 144px; top: 208px; width: 138px; height: 86px; }
  .front-label--large { left: 676px; top: 263px; width: 458px; height: 903px; }
  .front-label--small { left: 103px; top: 580px; width: 220px; height: 433px; }
  .label-type {
    font-family: "Alfa Slab One", serif;
    fill: var(--gold);
    stroke: var(--ink);
    stroke-width: 0.8;
    paint-order: stroke;
  }
  .label-type--dark {
    fill: var(--gold-deep);
    stroke: #4a3a22;
    stroke-width: 0.5;
  }
  .star-row {
    font-family: "Alfa Slab One", serif;
    fill: var(--gold-deep);
  }
</style>
</head>
<body>
<main class="canvas">

  <svg class="symbol-library" aria-hidden="true">
    <defs>
      <path id="label-outline" d="M95 0 H245 Q270 0 272 25 L275 95 C330 170 340 250 340 330 C340 420 320 480 280 560 L278 640 Q276 670 250 670 H90 Q64 670 62 640 L60 560 C20 480 0 420 0 330 C0 250 10 170 65 95 L68 25 Q70 0 95 0 Z"/>
      <radialGradient id="sunburst-tone" cx="50%" cy="50%" r="50%">
        <stop offset="0%" stop-color="var(--cream)"/>
        <stop offset="45%" stop-color="var(--sun)" stop-opacity="0.85"/>
        <stop offset="100%" stop-color="var(--paper)" stop-opacity="0"/>
      </radialGradient>
      <radialGradient id="barrel-tone" cx="50%" cy="50%" r="50%">
        <stop offset="0%" stop-color="var(--barrel)" stop-opacity="0.85"/>
        <stop offset="65%" stop-color="var(--barrel)" stop-opacity="0.45"/>
        <stop offset="100%" stop-color="var(--barrel)" stop-opacity="0"/>
      </radialGradient>
      <radialGradient id="ornament-tone" cx="50%" cy="55%" r="50%">
        <stop offset="0%" stop-color="var(--gold-deep)" stop-opacity="0.85"/>
        <stop offset="70%" stop-color="var(--gold)" stop-opacity="0.5"/>
        <stop offset="100%" stop-color="var(--gold)" stop-opacity="0"/>
      </radialGradient>
      <radialGradient id="flourish-tone" cx="50%" cy="50%" r="50%">
        <stop offset="0%" stop-color="var(--gold)" stop-opacity="0.55"/>
        <stop offset="100%" stop-color="var(--gold)" stop-opacity="0"/>
      </radialGradient>

      <symbol id="neck-label-art" viewBox="0 0 242 150">
        <path d="M18 4 H224 Q238 4 238 18 V110 Q238 146 200 146 H42 Q4 146 4 110 V18 Q4 4 18 4 Z"
              fill="var(--ink)" stroke="var(--gold)" stroke-width="5"/>
        <path d="M22 12 H220 Q230 12 230 22 V108 Q230 138 198 138 H44 Q12 138 12 108 V22 Q12 12 22 12 Z"
              fill="none" stroke="var(--gold)" stroke-width="1.2"/>
        <text class="label-type" x="121" y="62" text-anchor="middle" font-size="27">COPPER</text>
        <text class="label-type" x="121" y="100" text-anchor="middle" font-size="27">RIDGE</text>
        <ellipse cx="34" cy="110" rx="20" ry="16" fill="url(#flourish-tone)"
                 role="img" aria-label="Gold flourish ornament, left"/>
        <ellipse cx="208" cy="110" rx="20" ry="16" fill="url(#flourish-tone)"
                 role="img" aria-label="Gold flourish ornament, right"/>
      </symbol>

      <symbol id="front-label-art" viewBox="0 0 340 670">
        <use href="#label-outline" fill="var(--gold)"/>
        <use href="#label-outline" fill="var(--ink)" transform="translate(170 335) scale(0.97) translate(-170 -335)"/>
        <use href="#label-outline" fill="var(--gold)" transform="translate(170 335) scale(0.885) translate(-170 -335)"/>
        <use href="#label-outline" fill="var(--paper)" stroke="#d9c9a8" stroke-width="1.4" stroke-dasharray="1.5 2"
             transform="translate(170 335) scale(0.87) translate(-170 -335)"/>

        <text class="label-type label-type--dark" x="170" y="80" text-anchor="middle" font-size="17">37.5%</text>
        <text class="star-row" x="170" y="112" text-anchor="middle" font-size="15" letter-spacing="3">★★★★★</text>

        <ellipse cx="170" cy="300" rx="140" ry="180" fill="url(#sunburst-tone)"
                 role="img" aria-label="Faded sunburst behind two oak barrels"/>
        <ellipse cx="170" cy="275" rx="88" ry="58" fill="url(#barrel-tone)"
                 role="img" aria-label="Two oak barrels"/>

        <rect x="68" y="366" width="204" height="50" fill="var(--paper)" stroke="#3a2f20" stroke-width="2"/>
        <text class="label-type label-type--dark" x="170" y="402" text-anchor="middle" font-size="28">BOURBON</text>

        <text class="star-row" x="170" y="494" text-anchor="middle" font-size="15" letter-spacing="3">★★★★★</text>
        <ellipse cx="170" cy="545" rx="58" ry="36" fill="url(#ornament-tone)"
                 role="img" aria-label="Gold lotus ornament"/>
        <text class="label-type label-type--dark" x="170" y="618" text-anchor="middle" font-size="18">1L</text>
      </symbol>
    </defs>
  </svg>

  <!-- Small label set -->
  <svg class="neck-label neck-label--small" viewBox="0 0 242 150" aria-label="Copper Ridge neck label, small">
    <use href="#neck-label-art"/>
  </svg>
  <h2 class="brand-title brand-title--small">COPPER<br>RIDGE</h2>
  <svg class="front-label front-label--small" viewBox="0 0 340 670" aria-label="Copper Ridge bourbon front label, small">
    <use href="#front-label-art"/>
  </svg>

  <!-- Large label set -->
  <h1 class="brand-title brand-title--large">COPPER<br>RIDGE</h1>
  <svg class="neck-label neck-label--large" viewBox="0 0 242 150" aria-label="Copper Ridge neck label">
    <use href="#neck-label-art"/>
  </svg>
  <svg class="front-label front-label--large" viewBox="0 0 340 670" aria-label="Copper Ridge bourbon front label">
    <use href="#front-label-art"/>
  </svg>

</main>
</body>
</html>
```